Business Card Design for The KVZ Tunes

The KVZ Tunes is a platform which goal is to help emerging artists. At first, we were only promoting artists. But it rapidly become more than that. We've got now tons of project on the table, we're opening a store soon and are developing systems to manage

```html
<!DOCTYPE html>
<html lang="en">
<head>
<meta charset="UTF-8">
<title>The KVZ Tunes — Business Card</title>
<link rel="stylesheet" href="https://fonts.googleapis.com/css2?family=Michroma&display=swap">
<style>
  :root {
    --page-bg: #d8d3cb;
    --card-dark: #333333;
    --card-mid: #6b6b6b;
    --accent-gold: #e1aa1e;
    --text-light: #f2f2f2;
    --vinyl-deep: #1c1c1c;
    --vinyl-shine: #9a9a9a;
  }
  * { margin: 0; padding: 0; box-sizing: border-box; }
  html, body {
    width: 1200px;
    height: 1200px;
    overflow: hidden;
    background: var(--page-bg);
    font-family: "Michroma", sans-serif;
  }
  .card {
    position: absolute;
    left: 160px;
    width: 880px;
    height: 504px;
    overflow: hidden;
    box-shadow: 0 6px 18px rgba(0, 0, 0, 0.25);
  }
  .card-front { top: 76px; }
  .card-back {
    top: 620px;
    background: radial-gradient(ellipse at 45% 35%, var(--card-mid) 0%, #4c4c4c 45%, var(--card-dark) 100%);
  }
  .record-photo {
    position: absolute;
    inset: 0;
    background:
      linear-gradient(150deg, #d6d6d6 0%, #8c8c8c 18%, #4a4a4a 34%, var(--vinyl-shine) 52%, #2e2e2e 64%, var(--vinyl-deep) 82%, #3a3a3a 100%);
  }
  .front-url {
    position: absolute;
    left: 300px;
    top: 300px;
    color: var(--accent-gold);
    font-size: 15px;
    letter-spacing: 3px;
    text-transform: uppercase;
    transform: rotate(-36deg);
    transform-origin: left center;
    white-space: nowrap;
  }
  .brand {
    position: absolute;
    left: 70px;
    top: 215px;
    display: flex;
    align-items: center;
    gap: 16px;
  }
  .brand-dot {
    width: 64px;
    height: 64px;
    border-radius: 50%;
    background: var(--vinyl-deep);
  }
  .brand-name {
    color: var(--accent-gold);
    font-size: 18px;
    letter-spacing: 2px;
    text-transform: uppercase;
  }
  .identity {
    position: absolute;
    right: 62px;
    top: 92px;
    text-align: right;
  }
  .person-name {
    color: var(--accent-gold);
    font-size: 30px;
    letter-spacing: 3px;
    font-variant: small-caps;
  }
  .person-role {
    margin-top: 6px;
    color: var(--text-light);
    font-size: 15px;
    letter-spacing: 3px;
    text-transform: uppercase;
  }
  .contact-list {
    position: absolute;
    right: 62px;
    bottom: 70px;
    list-style: none;
    text-align: right;
    font-size: 15px;
    letter-spacing: 2px;
    line-height: 1.55;
    text-transform: uppercase;
  }
  .contact-label { color: var(--accent-gold); font-size: 13px; }
  .contact-value { color: var(--text-light); }
</style>
</head>
<body>
  <section class="card card-front">
    <div class="record-photo" role="img" aria-label="Close-up photograph of a spinning vinyl record's grooves in black and white"></div>
    <p class="front-url">www.thekvztunes.com</p>
  </section>

  <section class="card card-back">
    <div class="brand">
      <span class="brand-dot"></span>
      <span class="brand-name">The KVZ Tunes</span>
    </div>
    <div class="identity">
      <h1 class="person-name">Marcus Quill</h1>
      <p class="person-role">Consultant</p>
    </div>
    <ul class="contact-list">
      <li><span class="contact-label">voice:</span> <span class="contact-value">+882 417 09</span></li>
      <li><span class="contact-label">e-mail:</span> <span class="contact-value">m@thekvztunes.com</span></li>
      <li><span class="contact-label">web:</span> <span class="contact-value">thekvztunes.com</span></li>
    </ul>
  </section>
</body>
</html>
```